Kestrel Forge Tech
Bus. Cards/Stationary/Presentation
Kestrel Forge Tech - Information Technology
Creative Brief
Use specific fonts
Open to ideas on font pairing
Professional
Wendell Pask
Owner
218 Larkspur Avenue Suite 4400 Millbrook Falls, TX 79990
Wendell.Pask@kestrelforgetech.com
www.kestrelforgetech.com
I am open to my logo displayed on the back. I am also open to ideas on the back of business card. Be creative on front and back.

```html
<!DOCTYPE html>
<html lang="en">
<head>
<meta charset="utf-8">
<title>Kestrel Forge Tech – Business Cards</title>
<link href="https://fonts.googleapis.com/css2?family=Source+Sans+3:wght@400;600;700&display=swap" rel="stylesheet">
<style>
  :root {
    --backdrop: #2b2b2b;
    --card-white: #f7f7f7;
    --card-grey: #6f6f6f;
    --card-grey-dark: #5c5c5c;
    --brand-green: #5bb436;
    --brand-green-light: #8ccf5e;
    --brand-green-deep: #3f9a2a;
    --ink: #5a5a5a;
    --ink-soft: #7a7a7a;
    --white: #ffffff;
  }
  * { box-sizing: border-box; margin: 0; padding: 0; }
  html, body {
    width: 1200px; height: 792px; overflow: hidden;
    background: var(--backdrop);
    font-family: "Source Sans 3", "Helvetica Neue", Arial, sans-serif;
  }
  .card-sheet { position: relative; width: 1200px; height: 792px; }
  .card {
    position: absolute; width: 420px; height: 254px;
    border-radius: 12px; overflow: hidden;
  }
  .card--front { left: 150px; top: 128px; background: var(--card-white); }
  .card--logo-white { left: 630px; top: 128px; background: var(--card-white); }
  .card--grey { left: 150px; top: 414px; background: linear-gradient(180deg, var(--card-grey), var(--card-grey-dark)); }
  .card--green { left: 630px; top: 414px; background: radial-gradient(circle at 50% 40%, var(--brand-green-light), var(--brand-green) 55%, var(--brand-green-deep)); }

  .accent-band {
    position: absolute; left: 0; top: 0; bottom: 0; width: 22px;
    background: linear-gradient(90deg, var(--brand-green) 0 55%, var(--brand-green-light) 55% 100%);
  }

  .wordmark {
    display: flex; align-items: center; gap: 10px;
    font-weight: 700; color: var(--ink); white-space: nowrap;
  }
  .wordmark__dot { border-radius: 50%; background: var(--brand-green); flex: none; }
  .card--front .wordmark { position: absolute; left: 40px; top: 34px; font-size: 26px; }
  .card--front .wordmark__dot { width: 40px; height: 40px; }

  .contact {
    position: absolute; left: 104px; top: 138px;
    font-size: 10.5px; line-height: 14px; color: var(--ink);
  }
  .contact__row { display: flex; }
  .contact__label { width: 40px; font-weight: 700; }
  .contact__address { margin-bottom: 8px; }

  .person { position: absolute; left: 290px; top: 144px; }
  .person__name { font-size: 17px; font-weight: 700; color: var(--brand-green); }
  .person__role { font-size: 11px; color: var(--ink-soft); }

  .card--logo-white .wordmark {
    position: absolute; left: 0; right: 0; top: 88px; justify-content: center; font-size: 29px;
  }
  .card--logo-white .wordmark__dot { width: 46px; height: 46px; }

  .back-mark {
    position: absolute; left: 0; right: 0; top: 56px;
    display: flex; flex-direction: column; align-items: center; gap: 14px;
    color: var(--white); font-size: 24px; font-weight: 700;
  }
  .back-mark__dot { width: 70px; height: 70px; border-radius: 50%; background: var(--white); }

  .web {
    position: absolute; left: 0; right: 0; bottom: 24px; text-align: center;
    font-size: 11px; font-weight: 600; letter-spacing: 2px; color: var(--ink);
  }
  .card--grey .web, .card--green .web { color: var(--white); }
</style>
</head>
<body>
<main class="card-sheet">

  <section class="card card--front" aria-label="Business card front">
    <div class="accent-band"></div>
    <div class="wordmark"><span class="wordmark__dot"></span>Kestrel Forge Tech</div>
    <div class="contact">
      <p class="contact__address">218 Larkspur Avenue<br>Suite 4400, Millbrook Falls, TX 79990</p>
      <p class="contact__row"><span class="contact__label">Phone</span>: 555.555.0147</p>
      <p class="contact__row"><span class="contact__label">Cell</span>: 555.555.0182</p>
      <p class="contact__row"><span class="contact__label">Fax</span>: 555.555.0163</p>
      <p class="contact__row"><span class="contact__label">Email</span>: Wendell.Pask@kestrelforgetech.com</p>
      <p class="contact__row"><span class="contact__label">Web</span>: www.kestrelforgetech.com</p>
    </div>
    <div class="person">
      <p class="person__name">Wendell Pask</p>
      <p class="person__role">Owner</p>
    </div>
  </section>

  <section class="card card--logo-white" aria-label="Business card back, white">
    <div class="wordmark"><span class="wordmark__dot"></span>Kestrel Forge Tech</div>
    <p class="web">www.kestrelforgetech.com</p>
  </section>

  <section class="card card--grey" aria-label="Business card back, grey">
    <div class="back-mark"><span class="back-mark__dot"></span>Kestrel Forge Tech</div>
    <p class="web">www.kestrelforgetech.com</p>
  </section>

  <section class="card card--green" aria-label="Business card back, green">
    <div class="back-mark"><span class="back-mark__dot"></span>Kestrel Forge Tech</div>
    <p class="web">www.kestrelforgetech.com</p>
  </section>

</main>
</body>
</html>
```